Looking for an ecommerce website that specifically sells 1 product (Rapid Blue Comet Prime).... We do not need any shopping cart as we will be linking to our Corvana listing for purchasing.... similar to how this site does it:
http://www.plomaxen.com/
I want the following pages:
Home
Order
FAQ- we can take the copy from this site: http://quickbluecomet.com/
Contact us: just a basic contact form that will forward emails to contact@rbcprime-mail.com
Here is the layout design I want to copy:
http://www.plomaxen.com/
Of course we will use different colors to match this specific theme from the blue comet box, Black and Red
I also want to incorporate a design element from this site:
https://www.balduran.com/
As you can see, as you scroll down the page to read the copy, there is a left side panel that has the image of the product and the buying options available and a buy now for each one⦠please do the same on this new site..
Buying options:
FREE SHIPPING ON ALL ORDERS!
Preferred Package: Buy 5 get 1 free- 224.75
Power Package: 3 boxes (30 capsules)- 129.99
Intro Package: 1 box 10 capsules- $44.95
For copy for the site, we can get it from here:
http://quickbluecomet.com/
Some catch phrases to use:
100% Money Back Guarantee
QLB Certified Laboratory
100% All Natural Ingredients
Fast Acting
IMPORTANT- DO NOT USE ANY OF THE COPY THAT IS RELATED TO DEER ANTLER AS WE HAVE REMOVED THIS INGREDIENT FROM THE PRODUCT
I have attached images of the actual product here as well

```html
<!DOCTYPE html>
<html lang="en">
<head>
<meta charset="utf-8">
<title>Blue Comet Prime — Home</title>
<link rel="stylesheet" href="https://fonts.googleapis.com/css2?family=Merriweather:wght@400;700;900&family=Roboto:wght@400;500;700&display=swap">
<style>
  :root{
    --red:#b3121c;
    --red-dark:#8e0d14;
    --ink:#222;
    --text:#5a5a5a;
    --muted:#8a8a8a;
    --line:#dcdcdc;
    --paper:#f6f5f4;
    --panel:#ffffff;
    --black:#151515;
  }
  *{box-sizing:border-box;margin:0;padding:0}
  html,body{width:696px;height:1200px;overflow:hidden;background:var(--paper)}
  body{font-family:"Roboto",Arial,sans-serif;color:var(--ink)}
  .canvas{position:relative;width:696px;height:1200px;overflow:hidden;background:linear-gradient(#f7f6f5,#efedec)}
  .abs{position:absolute}

  /* header */
  .site-header{left:0;top:0;width:696px;height:56px;background:#fbfaf9;border-bottom:1.5px solid var(--red)}
  .brand{font-family:"Merriweather",Georgia,serif;font-weight:900;color:var(--red);font-size:15px;line-height:15px;letter-spacing:.3px;white-space:nowrap}
  .brand-dot{display:inline-block;width:9px;height:9px;border-radius:50%;background:var(--red);margin-right:5px;vertical-align:1px}
  .topbar{right:57px;top:11px;font-size:8.2px;color:#333;display:flex;gap:9px;align-items:center}
  .topbar svg{width:7px;height:7px;fill:var(--red);margin-right:3px;vertical-align:-1px}
  .nav{right:57px;top:33px;display:flex;gap:18px;font-size:9.3px;font-weight:500;letter-spacing:.2px}
  .nav .active{color:var(--red)}

  /* hero */
  .hero{left:0;top:57px;width:696px;height:280px;background:linear-gradient(90deg,#f3efed 0%,#efe8e4 45%,#e9ddd6 100%)}
  .hero-photo{left:330px;top:57px;width:366px;height:280px;background:linear-gradient(100deg,#efe6e1 0%,#e2cdbf 30%,#c89f86 55%,#8d6552 80%,#5b3e32 100%)}
  .product-box{background:linear-gradient(135deg,#242424,#0c0c0c);border:1px solid #000;box-shadow:2px 3px 6px rgba(0,0,0,.35)}
  .hero-box{left:32px;top:102px;width:133px;height:188px}
  .hero-kicker{left:200px;top:106px;font-family:"Merriweather",Georgia,serif;font-size:18px;color:var(--ink)}
  .hero-title{left:200px;top:130px;font-family:"Merriweather",Georgia,serif;font-weight:900;font-size:36px;color:var(--red);letter-spacing:.5px;white-space:nowrap}
  .hero-offer{left:200px;top:178px;font-family:"Merriweather",Georgia,serif;font-size:14px;color:var(--ink)}
  .btn-outline{display:flex;align-items:center;justify-content:center;gap:4px;border:1.5px solid var(--red);color:var(--red);font-weight:700;background:transparent}
  .btn-outline svg{width:8px;height:8px}
  .hero-btn{left:201px;top:226px;width:87px;height:28px;font-size:10.5px}

  /* sidebar */
  .sidebar{left:58px;top:371px;width:228px;height:594px;background:var(--panel);border:1px solid #d9d6d4;box-shadow:0 0 4px rgba(0,0,0,.08)}
  .shipping{left:58px;top:371px;width:228px;height:64px;background:#f2f0ef;border-bottom:1px solid #d7d4d2;box-shadow:0 2px 3px rgba(0,0,0,.1)}
  .shipping svg{position:absolute;left:12px;top:14px}
  .shipping-text{left:148px;top:384px;width:132px;text-align:center;font-weight:500;font-size:12.8px;line-height:19px;color:#333}
  .side-box{left:74px;top:454px;width:67px;height:94px}
  .seal{left:72px;top:532px;width:31px;height:31px;border-radius:50%;background:radial-gradient(circle,#1f5e96 55%,#5b9ac8 60%,#1f5e96 70%);border:1px solid #12406a}
  .features{left:157px;top:453px;width:116px;list-style:none}
  .features li{font-size:7.2px;color:#444;height:21.5px;line-height:20px;border-bottom:1px dashed #e2c9c9;display:flex;align-items:center;gap:5px;white-space:nowrap}
  .features li::before{content:"";width:6px;height:6px;border-radius:50%;background:var(--red);flex:none}
  .order-title{left:70px;top:578px;font-family:"Merriweather",Georgia,serif;font-weight:700;font-variant:small-caps;font-size:11px;color:var(--ink)}
  .package{left:70px;width:203px;height:58px;border:1px solid #e0dedd;background:#fafafa}
  .package.featured{background:var(--red-dark);border-color:var(--red-dark);color:#fff}
  .package .thumb{position:absolute;left:6px;top:5px;width:36px;height:48px}
  .package .name{position:absolute;left:53px;top:8px;font-size:10px;font-weight:500}
  .package .note{position:absolute;left:53px;top:22px;font-size:7px;color:#666}
  .package.featured .note{color:#f0d3d3}
  .package .price{position:absolute;left:53px;top:38px;font-size:12px;font-weight:700;color:var(--red)}
  .package.featured .price{color:#fff}
  .package .check{position:absolute;left:164px;top:9px;width:11px;height:10px;border:1.5px solid var(--red);background:#fff}
  .package .select{position:absolute;left:152px;top:22px;font-size:6.8px;color:#555}
  .package.featured .select{color:#fff}
  .package .submit{position:absolute;left:146px;top:34px;width:49px;height:15px;background:var(--red);color:#fff;font-size:7.5px;font-weight:700;text-align:center;line-height:15px}
  .package.featured .submit{background:#1a1a1a}
  .cta{left:70px;top:811px;width:203px;height:64px;background:var(--black);color:#fff;text-align:center;font-weight:500;font-size:13px;line-height:19px;padding-top:13px}
  .cta .mark{color:var(--red);text-decoration:underline}
  .badge-lab{left:70px;top:889px;width:70px;height:57px;background:linear-gradient(#fff 0 55%,#10285a 55%);border:1px solid #10285a}
  .badge-natural{left:150px;top:888px;width:58px;height:58px;border-radius:50%;background:radial-gradient(circle,#3c8c24 52%,#d7b23a 56%,#b48a1c 70%)}
  .badge-money{left:216px;top:888px;width:58px;height:58px;border-radius:50%;background:radial-gradient(circle,#1d1d1d 40%,#d6a53a 45%,#a77818 70%)}

  /* content */
  .section-title{font-family:"Merriweather",Georgia,serif;font-weight:700;font-size:19px;color:var(--ink)}
  .about-title{left:313px;top:366px}
  .about-sub{left:313px;top:398px;font-size:12px;color:#333}
  .about-sub em{font-style:normal;color:var(--red)}
  .copy{font-size:7.4px;line-height:13.5px;color:var(--text);text-align:justify}
  .about-copy{left:313px;top:427px;width:325px}
  .about-copy .link{color:var(--red)}
  .video{left:313px;top:498px;width:325px;height:161px;border:3px solid #fff;box-shadow:0 0 3px rgba(0,0,0,.3);background:linear-gradient(120deg,#d8cdc6 0%,#b39485 35%,#7b5a4c 60%,#cbbfb8 100%)}
  .video-label{left:322px;top:505px;font-size:9px;color:#222;font-weight:500}
  .play{left:459px;top:567px;width:34px;height:24px;border-radius:6px;background:#d91c1c}
  .fast-title{left:313px;top:679px}
  .fast-copy{left:313px;top:712px;width:205px}
  .fast-pack{left:524px;top:683px;width:136px;height:150px;background:linear-gradient(160deg,#2a2a2a 0%,#111 55%,#8c8a84 75%,#c8c3b4 100%);border-radius:3px}
  .btn-sm{height:24px;font-size:8.8px}
  .fast-btn{left:313px;top:808px;width:71px}
  .label-box{left:313px;top:857px;width:79px;height:113px}
  .ants-copy{left:407px;top:857px;width:231px}
  .ants-btn{left:407px;top:945px;width:71px}

  /* footer */
  .site-footer{left:0;top:1019px;width:696px;height:181px;background:linear-gradient(#efeceb,#e9e6e5);border-top:1.5px solid var(--red)}
  .footer-brand{left:56px;top:1067px;font-size:19px;line-height:20px}
  .footer-brand .brand-dot{width:12px;height:12px}
  .footer-head{top:1058px;font-size:10px;font-weight:500;color:#222;letter-spacing:.2px}
  .social{left:290px;top:1083px;display:flex;gap:7px}
  .social span{width:26px;height:26px;border-radius:50%;display:block;box-shadow:0 1px 2px rgba(0,0,0,.2)}
  .s1{background:#223d70}.s2{background:#2aa8d8}.s3{background:#cf1b1b}
  .email{left:465px;top:1081px;width:173px;height:24px;border:1px solid #c9c6c4;background:#fff;font-size:7.5px;color:#888;padding:8px 10px}
  .email svg{position:absolute;right:8px;top:8px}
  .subscribe{left:465px;top:1111px;width:72px;height:23px;background:var(--red);color:#fff;font-size:8.5px;font-weight:700;text-align:center;line-height:23px}
  .footer-rule{left:56px;top:1152px;width:582px;height:1px;background:#cfcbc9}
  .copyright{left:0;top:1173px;width:696px;text-align:center;font-size:8px;color:#333}
</style>
</head>
<body>
<div class="canvas">

  <header class="abs site-header"></header>
  <div class="abs brand" style="left:57px;top:21px"><span class="brand-dot"></span>BLUE COMET PRIME</div>
  <div class="abs topbar">
    <span><svg viewBox="0 0 10 10"><path d="M2 0l2 2-1 1.5c.7 1.4 1.6 2.3 3 3L7.5 5.5 10 7.5 8.5 10C4 9.5.5 6 0 1.5z"/></svg>Contact: 1-888 555-0187</span><span>|</span>
    <span><svg viewBox="0 0 10 10"><circle cx="5" cy="3" r="2.6"/><path d="M0 10c0-3 2.2-4.5 5-4.5S10 7 10 10z"/></svg>My Account</span>
  </div>
  <nav class="abs nav"><span class="active">HOME</span><span>PRODUCTS</span><span>ORDER</span><span>FAQ</span><span>CONTACT US</span></nav>

  <section class="abs hero"></section>
  <div class="abs hero-photo" role="img" aria-label="Photograph of a couple embracing"></div>
  <div class="abs product-box hero-box" role="img" aria-label="Blue Comet Prime product box, black with red design"></div>
  <div class="abs hero-kicker">Instant</div>
  <div class="abs hero-title">BLUE COMET</div>
  <div class="abs hero-offer">Buy 5 get 1 free</div>
  <div class="abs btn-outline hero-btn">BUY NOW <svg viewBox="0 0 10 10"><circle cx="5" cy="5" r="5" fill="#b3121c"/><path d="M4 2.5L6.5 5 4 7.5" stroke="#fff" stroke-width="1.5" fill="none"/></svg></div>

  <aside class="abs sidebar"></aside>
  <div class="abs shipping">
    <svg width="76" height="36" viewBox="0 0 76 36">
      <rect x="0" y="8" width="16" height="3" fill="#b3121c"/><rect x="4" y="15" width="14" height="3" fill="#b3121c"/><rect x="8" y="22" width="10" height="3" fill="#b3121c"/>
      <rect x="20" y="4" width="34" height="24" rx="2" fill="#b3121c"/>
      <path d="M55 10h10l8 9v9H55z" fill="#222"/><rect x="58" y="13" width="7" height="6" fill="#fff"/>
      <circle cx="30" cy="30" r="5" fill="#222"/><circle cx="30" cy="30" r="2" fill="#fff"/>
      <circle cx="64" cy="30" r="5" fill="#222"/><circle cx="64" cy="30" r="2" fill="#fff"/>
    </svg>
  </div>
  <div class="abs shipping-text">FREE SHIPPING ON ALL ORDERS!</div>
  <div class="abs product-box side-box" role="img" aria-label="Blue Comet Prime product box"></div>
  <div class="abs seal" role="img" aria-label="One year seal"></div>
  <ul class="abs features">
    <li>100% Natural Ingredients</li>
    <li>Starts Working Within 10 minites</li>
    <li>Effects can be Felt for 4 days</li>
    <li>Can br taken with alcohol</li>
    <li>Prolongs Sexual Performance</li>
  </ul>
  <div class="abs order-title">Select Your Order:</div>

  <div class="abs package" style="top:601px">
    <div class="product-box thumb" role="img" aria-label="Product box"></div>
    <div class="name">Preferred Package</div><div class="note">(Buy 5 get 1 free)</div>
    <div class="price">$ 224.75</div>
    <div class="check"></div><div class="select">Select order</div><div class="submit">SUBMIT</div>
  </div>
  <div class="abs package featured" style="top:668px">
    <div class="product-box thumb" role="img" aria-label="Product box"></div>
    <div class="name">Power Package</div><div class="note">(3 boxes 30 capsules)</div>
    <div class="price">$ 129.99</div>
    <div class="check"></div><div class="select">Select order</div><div class="submit">SUBMIT</div>
  </div>
  <div class="abs package" style="top:735px">
    <div class="product-box thumb" role="img" aria-label="Product box"></div>
    <div class="name">Intro Package</div><div class="note">(1 box 10 capsules)</div>
    <div class="price">$ 44.95</div>
    <div class="check"></div><div class="select">Select order</div><div class="submit">SUBMIT</div>
  </div>

  <div class="abs cta">Enhance Your Confidence Now<br>Buy <span class="mark">BLUE COMET</span> Today</div>
  <div class="abs badge-lab" role="img" aria-label="QLB approved laboratory badge"></div>
  <div class="abs badge-natural" role="img" aria-label="100% natural badge"></div>
  <div class="abs badge-money" role="img" aria-label="Money back guarantee badge"></div>

  <h2 class="abs section-title about-title">ABOUT BLUE COMET</h2>
  <div class="abs about-sub">The Little Known Secret <em>"HERB OF KINGS"</em></div>
  <p class="abs copy about-copy">Ever heard of this Chinese Medicinal Classic called "Yao Cao Zhen Lu" written by the famed 'granddaddy of Traditional Chinese Medicine", Lu Ming Tao? Well, in it, Uncle Lu reveals what he considers to be the herb of the highest order used by only Emperors and Noblemen as clearly stated in Imperial Records..... <span class="link">Guess what it is?</span></p>
  <div class="abs video" role="img" aria-label="Video still of a couple embracing"></div>
  <div class="abs video-label">INSTANT BLUE COMET</div>
  <div class="abs play"><svg width="34" height="24" viewBox="0 0 34 24"><path d="M13 7l9 5-9 5z" fill="#fff"/></svg></div>

  <h2 class="abs section-title fast-title">FAST ACTING</h2>
  <p class="abs copy fast-copy">With your permission (and with strict precautions for privacy), I'm gonna reveal the most important and exciting breakthroughs in male sexual health. News of this breakthrough is spreading like wildfire among men in every age group. In fact, this breakthrough is so radical, it has astonished the doctors and sex experts who discovered it!</p>
  <div class="abs fast-pack" role="img" aria-label="Three product boxes with a capsule blister pack"></div>
  <div class="abs btn-outline btn-sm fast-btn">BUY NOW <svg viewBox="0 0 10 10"><circle cx="5" cy="5" r="5" fill="#b3121c"/><path d="M4 2.5L6.5 5 4 7.5" stroke="#fff" stroke-width="1.5" fill="none"/></svg></div>

  <div class="abs product-box label-box" role="img" aria-label="Back of the product box with ingredient label"></div>
  <p class="abs copy ants-copy">Apparently ants are a superior tonic with such excellent curative powers that it's various beneficial effects include: increased strength, energy, stamina; strengthens the nervous system, digestive functions, detoxification functions and muscular system; boosts mental and physical energy.</p>
  <div class="abs btn-outline btn-sm ants-btn">BUY NOW <svg viewBox="0 0 10 10"><circle cx="5" cy="5" r="5" fill="#b3121c"/><path d="M4 2.5L6.5 5 4 7.5" stroke="#fff" stroke-width="1.5" fill="none"/></svg></div>

  <footer class="abs site-footer"></footer>
  <div class="abs brand footer-brand"><span class="brand-dot"></span>BLUE COMET PRIME</div>
  <div class="abs footer-head" style="left:290px">FOLLOW US ON</div>
  <div class="abs social"><span class="s1" aria-label="Social link"></span><span class="s2" aria-label="Social link"></span><span class="s3" aria-label="Social link"></span></div>
  <div class="abs footer-head" style="left:465px">NEWSLETTER SUBSCRIBE</div>
  <div class="abs email">Enter Email<svg width="9" height="7" viewBox="0 0 9 7"><rect width="9" height="7" fill="#888"/><path d="M0 0l4.5 3.5L9 0" stroke="#fff" fill="none"/></svg></div>
  <div class="abs subscribe">SUBSCRIBE</div>
  <div class="abs footer-rule"></div>
  <div class="abs copyright">Copyrights © 2018 Blue Comet Prime.&nbsp; All Rights Reserved&nbsp;&nbsp; | &nbsp;&nbsp;Privacy Policy.</div>

</div>
</body>
</html>
```